Pelarix PowerPoint Theme/Template

I want to be able to put together presentations that have a cohesive look and work with my current branding on my website (www.pelarix.com) and social media (#pelarixskincare).

```html
<!DOCTYPE html>
<html lang="en">
<head>
<meta charset="utf-8">
<title>Pelarix Presentation Theme</title>
<link href="https://fonts.googleapis.com/css2?family=Playfair+Display:wght@700;900&family=Poppins:wght@300;400;500;600;700&display=swap" rel="stylesheet">
<style>
:root{
  --canvas:#d8d9dc;
  --paper:#ffffff;
  --brown-dark:#6f3c17;
  --brown:#9b5b27;
  --brown-soft:#c08a5c;
  --ink:#4f4640;
  --muted:#8a7f78;
  --line:#e3d6cb;
}
*{margin:0;padding:0;box-sizing:border-box}
html,body{width:1051px;height:1200px;overflow:hidden;background:var(--canvas)}
.board{position:relative;width:1051px;height:1200px}
.slide{position:absolute;width:318px;height:179px;background:var(--paper);overflow:hidden;box-shadow:0 2px 5px rgba(0,0,0,.18);font-family:'Poppins',sans-serif;color:var(--ink)}
.col1{left:36px}.col2{left:367px}.col3{left:697px}
.row1{top:29px}.row2{top:222px}.row3{top:415px}.row4{top:608px}.row5{top:801px}.row6{top:992px}
.abs{position:absolute}
.brand{position:absolute;top:7px;right:9px;text-align:center;font-family:'Playfair Display',serif;font-weight:900;font-size:8px;line-height:1;color:var(--brown)}
.brand-by{display:block;font-family:'Poppins',sans-serif;font-weight:400;font-size:2.2px;margin-top:1px;color:var(--brown)}
.page{position:absolute;right:8px;bottom:6px;font-size:3.4px;color:var(--muted)}
.title{position:absolute;font-family:'Playfair Display',serif;font-weight:900;color:var(--brown-dark);line-height:1.05}
.rule{position:absolute;height:2px;background:var(--brown)}
.text{position:absolute;font-size:3.1px;line-height:1.4;color:var(--muted)}
.label{font-weight:600;color:var(--brown);font-size:4.4px}
.photo{position:absolute}
.warm{background:linear-gradient(135deg,#f1e4d8,#cfa987 60%,#a8774f)}
.pale{background:linear-gradient(135deg,#f6efe9,#dcc6b3)}
.cool{background:linear-gradient(135deg,#3f6fa8,#c8b08a 55%,#e9dcc9)}
.teal{background:linear-gradient(135deg,#8a4d2a,#c6a48a 50%,#9fb6bf)}
.fill-dark{background:var(--brown-dark)}
.fill-mid{background:var(--brown)}
.white{color:#fff}
.num-box{position:absolute;width:10px;height:10px;background:var(--brown);color:#fff;font-size:5px;font-weight:700;text-align:center;line-height:10px}
.num-dot{position:absolute;width:17px;height:17px;border-radius:50%;background:var(--brown);color:#fff;font-size:7px;font-weight:600;text-align:center;line-height:17px}
.icon-box{position:absolute;width:24px;height:24px;background:var(--brown);border:1px solid var(--brown-dark)}
.icon-box svg{width:100%;height:100%}
.overlay{position:absolute;left:0;top:0;width:318px;height:179px}
</style>
</head>
<body>
<div class="board">

<!-- 01 Cover -->
<section class="slide col1 row1">
  <div class="abs" style="left:7px;top:7px;width:8px;height:8px;background:#e8dfd7"></div>
  <div class="abs" style="left:15px;top:28px;font-family:'Playfair Display',serif;font-weight:900;font-size:21px;color:var(--brown);line-height:1">Pelarix</div>
  <div class="abs" style="left:30px;top:50px;font-size:5px;color:var(--brown)">by dr. elena marlow</div>
  <div class="abs" style="left:21px;top:100px;font-size:13px;font-weight:300;color:var(--brown-dark);line-height:1">Love For</div>
  <div class="abs" style="left:21px;top:114px;font-family:'Playfair Display',serif;font-weight:900;font-size:19px;color:var(--brown);line-height:1.05">Your Skin</div>
  <div class="abs" style="left:19px;top:162px;width:3px;height:3px;border-radius:50%;background:#e6d6c8"></div>
  <div class="abs" style="left:25px;top:162px;width:3px;height:3px;border-radius:50%;background:var(--brown)"></div>
  <div class="abs" style="left:31px;top:162px;width:3px;height:3px;border-radius:50%;background:#e6d6c8"></div>
  <div class="photo warm" role="img" aria-label="Woman in a bathrobe applying face cream" style="left:134px;top:0;width:184px;height:152px"></div>
  <div class="abs fill-mid" style="left:134px;top:152px;width:184px;height:27px;color:#fff;font-size:7px;letter-spacing:2.6px;text-align:center;line-height:27px">pelarix.com</div>
</section>

<!-- 02 Agenda -->
<section class="slide col2 row1">
  <div class="brand">Pelarix<span class="brand-by">by dr. elena marlow</span></div>
  <div class="title" style="left:57px;top:18px;font-size:14px">Agenda</div>
  <div class="rule" style="left:64px;top:40px;width:32px"></div>
  <div class="photo warm" role="img" aria-label="Woman receiving a facial mask treatment beside a candle" style="left:28px;top:42px;width:106px;height:116px"></div>
  <div class="abs" style="left:149px;top:45px;width:130px">
    <div class="label">1. <span style="font-weight:500">Lorem ipsum</span></div>
    <div class="text" style="position:static;margin:1px 0 0 8px">Lorem ipsum dolor sit amet, consectetuer adipiscing elit, sed diam nonummy nibh euismod tincid</div>
  </div>
  <div class="abs" style="left:149px;top:75px;width:130px">
    <div class="label">2. <span style="font-weight:500">Lorem ipsum</span></div>
    <div class="text" style="position:static;margin:1px 0 0 8px">Lorem ipsum dolor sit amet, consectetuer adipiscing elit, sed diam nonummy nibh euismod tincid</div>
  </div>
  <div class="abs" style="left:149px;top:104px;width:130px">
    <div class="label">3. <span style="font-weight:500">Lorem ipsum</span></div>
    <div class="text" style="position:static;margin:1px 0 0 8px">Lorem ipsum dolor sit amet, consectetuer adipiscing elit, sed diam nonummy nibh euismod tincid</div>
  </div>
  <div class="abs" style="left:149px;top:133px;width:130px">
    <div class="label">4. <span style="font-weight:500">Lorem ipsum</span></div>
    <div class="text" style="position:static;margin:1px 0 0 8px">Lorem ipsum dolor sit amet, consectetuer adipiscing elit, sed diam nonummy nibh euismod tincid</div>
  </div>
  <div class="page">02</div>
</section>

<!-- 03 Subject title -->
<section class="slide col3 row1">
  <div class="abs fill-mid" style="left:0;top:0;width:160px;height:12px"></div>
  <div class="brand">Pelarix<span class="brand-by">by dr. elena marlow</span></div>
  <div class="title" style="left:16px;top:21px;font-size:13px">Subject<br>Title</div>
  <div class="rule" style="left:16px;top:63px;width:18px;height:1.5px"></div>
  <div class="text" style="left:16px;top:72px;width:72px;color:var(--ink)">Lorem ipsum dolor sit amet, consectetuer adipiscing elit, sed diam nonummy nibh euismod tincidunt ut laoreet dolore magna aliquam erat volutpat. Ut wisi enim ad minim veniam, quis nostrud exerci tation ullamcorper suscipit lobortis nisl ut aliquip ex ea commodo consequat. Duis autem vel eum iriure.</div>
  <div class="photo pale" role="img" aria-label="Woman with a towel wrapped on her head" style="left:90px;top:18px;width:65px;height:90px"></div>
  <div class="abs fill-mid" style="left:134px;top:42px;width:184px;height:94px"></div>
  <div class="photo warm" role="img" aria-label="Woman wrapped in a towel touching her shoulder" style="left:166px;top:55px;width:63px;height:103px"></div>
  <div class="abs white" style="left:236px;top:55px;font-size:8px;font-weight:500;line-height:1.15">Lorem Ipsum<br>Dolor Sit<br>Ametkeeper.</div>
  <div class="text white" style="left:236px;top:93px;width:62px">Lorem ipsum dolor sit amet, consectetuer adipiscing<br><br>elit, sed diam nonummy nibh euismod tincidunt ut laoreet dolore magna</div>
  <div class="page">03</div>
</section>

<!-- 04 Values -->
<section class="slide col1 row2">
  <div class="abs fill-dark" style="left:0;top:0;width:127px;height:179px"></div>
  <div class="brand">Pelarix<span class="brand-by">by dr. elena marlow</span></div>
  <div class="title white" style="left:19px;top:29px;font-size:13px;line-height:1.45;color:#fff">Lorem Ipsum<br>Dolor Sit<br>Ametkeeper.</div>
  <div class="rule" style="left:19px;top:94px;width:15px;height:1.5px;background:var(--brown-soft)"></div>
  <div class="text" style="left:19px;top:106px;width:95px;color:#f1e2d5">Lorem ipsum dolor sit amet, consectetuer adipiscing elit, sed diam nonummy nibh euismod tincidunt erat volutpat.<br><br>Ut wisi enim ad minim veniam, quis nostrud exerci tation ullamcorper suscipit lobortis nisl ut aliquip ex ea commodo consequat.</div>
  <div class="icon-box" style="left:144px;top:34px;width:22px;height:22px"><svg viewBox="0 0 22 22"><circle cx="8" cy="9" r="2.4" fill="#fff"/><circle cx="14" cy="9" r="2.4" fill="#fff"/><path d="M4 16c0-3 2-4.5 4-4.5s4 1.5 4 4.5zM10 16c0-3 2-4.5 4-4.5s4 1.5 4 4.5z" fill="#fff"/></svg></div>
  <div class="abs" style="left:177px;top:37px;width:115px"><div style="font-size:6px;font-weight:600;color:var(--brown-dark)">We Before Me</div><div class="text" style="position:static">ipsum dolor sit amet, cons ectetuer adipiscing elit, sed diam nonummy nibh euismod tincidunt ut laoreet</div></div>
  <div class="icon-box" style="left:144px;top:79px;width:22px;height:22px"><svg viewBox="0 0 22 22"><circle cx="8" cy="6" r="2" fill="#fff"/><circle cx="14" cy="6" r="2" fill="#fff"/><rect x="6" y="9" width="4" height="9" fill="#fff"/><rect x="12" y="9" width="4" height="9" fill="#fff"/></svg></div>
  <div class="abs" style="left:177px;top:81px;width:118px"><div style="font-size:6px;font-weight:600;color:var(--brown-dark)">We Are Good People</div><div class="text" style="position:static">ipsum dolor sit amet, cons ectetuer adipiscing elit, sed diam nonummy nibh euismod tincidunt ut laoreet dolore magna aliquam erat volutpat.</div></div>
  <div class="icon-box" style="left:144px;top:124px;width:22px;height:22px"><svg viewBox="0 0 22 22"><path d="M11 12l-3.5-3.3a2 2 0 0 1 3-2.6l.5.6.5-.6a2 2 0 0 1 3 2.6z" fill="#fff"/><path d="M4 14h5l3 2h6v2H4z" fill="#fff"/></svg></div>
  <div class="abs" style="left:177px;top:126px;width:115px"><div style="font-size:6px;font-weight:600;color:var(--brown-dark)">We Work with Heart</div><div class="text" style="position:static">ipsum dolor sit amet, cons ectetuer adipiscing elit, sed diam nonummy nibh euismod tincidunt</div></div>
  <div class="page">04</div>
</section>

<!-- 05 Icon grid -->
<section class="slide col2 row2">
  <div class="brand">Pelarix<span class="brand-by">by dr. elena marlow</span></div>
  <div class="title" style="left:9px;top:11px;font-size:11px">Text Added Here</div>
  <div class="rule" style="left:9px;top:27px;width:22px;height:1.5px"></div>
  <div class="icon-box" style="left:55px;top:40px"><svg viewBox="0 0 24 24"><circle cx="9" cy="10" r="2.5" fill="none" stroke="#fff" stroke-width=".8"/><circle cx="15" cy="10" r="2.5" fill="none" stroke="#fff" stroke-width=".8"/><path d="M5 17c0-3 2-4 4-4s4 1 4 4M11 17c0-3 2-4 4-4s4 1 4 4" fill="none" stroke="#fff" stroke-width=".8"/></svg></div>
  <div class="icon-box" style="left:145px;top:40px"><svg viewBox="0 0 24 24"><circle cx="10" cy="12" r="4" fill="none" stroke="#fff" stroke-width=".8"/><circle cx="15" cy="9" r="3" fill="none" stroke="#fff" stroke-width=".8"/><path d="M7 18h6" stroke="#fff" stroke-width=".8"/></svg></div>
  <div class="icon-box" style="left:235px;top:40px"><svg viewBox="0 0 24 24"><path d="M6 18V14M10 18V12M14 18V10M18 18V7M5 13l5-4 3 2 5-5" fill="none" stroke="#fff" stroke-width=".9"/></svg></div>
  <div class="icon-box" style="left:55px;top:103px"><svg viewBox="0 0 24 24"><path d="M6 5v14h13M8 8l4 6 3-1 3 4" fill="none" stroke="#fff" stroke-width=".9"/></svg></div>
  <div class="icon-box" style="left:145px;top:103px"><svg viewBox="0 0 24 24"><path d="M9 7h6l-1.5 2.5c3 1.5 4.5 4 4.5 6.5 0 2-1.5 3-6 3s-6-1-6-3c0-2.5 1.5-5 4.5-6.5z" fill="none" stroke="#fff" stroke-width=".9"/><text x="12" y="17" font-size="5" fill="#fff" text-anchor="middle" font-family="Poppins">$</text></svg></div>
  <div class="icon-box" style="left:235px;top:103px"><svg viewBox="0 0 24 24"><circle cx="12" cy="10" r="5" fill="none" stroke="#fff" stroke-width=".9"/><path d="M9 14l-2 5 3-1 2 2 0-4M15 14l2 5-3-1-2 2" fill="none" stroke="#fff" stroke-width=".8"/></svg></div>
  <div class="abs" style="left:37px;top:68px;width:60px;text-align:center"><div class="label" style="font-weight:500">Lorem ipsum</div><div class="text" style="position:static">Lorem ipsum dolor sit amet, consectetuer adipiscing elit, sed diam nonummy nibh euismod tincidunt ut laoreet</div></div>
  <div class="abs" style="left:127px;top:68px;width:60px;text-align:center"><div class="label" style="font-weight:500">Lorem ipsum</div><div class="text" style="position:static">Lorem ipsum dolor sit amet, consectetuer adipiscing elit, sed diam nonummy nibh euismod tincidunt ut laoreet</div></div>
  <div class="abs" style="left:217px;top:68px;width:60px;text-align:center"><div class="label" style="font-weight:500">Lorem ipsum</div><div class="text" style="position:static">Lorem ipsum dolor sit amet, consectetuer adipiscing elit, sed diam nonummy nibh euismod tincidunt ut laoreet</div></div>
  <div class="abs" style="left:37px;top:131px;width:60px;text-align:center"><div class="label" style="font-weight:500">Lorem ipsum</div><div class="text" style="position:static">Lorem ipsum dolor sit amet, consectetuer adipiscing elit, sed diam nonummy nibh euismod tincidunt ut laoreet</div></div>
  <div class="abs" style="left:127px;top:131px;width:60px;text-align:center"><div class="label" style="font-weight:500">Lorem ipsum</div><div class="text" style="position:static">Lorem ipsum dolor sit amet, consectetuer adipiscing elit, sed diam nonummy nibh euismod tincidunt ut laoreet</div></div>
  <div class="abs" style="left:217px;top:131px;width:60px;text-align:center"><div class="label" style="font-weight:500">Lorem ipsum</div><div class="text" style="position:static">Lorem ipsum dolor sit amet, consectetuer adipiscing elit, sed diam nonummy nibh euismod tincidunt ut laoreet</div></div>
  <div class="page">05</div>
</section>

<!-- 06 About us -->
<section class="slide col3 row2">
  <div class="brand">Pelarix<span class="brand-by">by dr. elena marlow</span></div>
  <div class="title" style="left:14px;top:10px;font-size:12px">About Us</div>
  <div class="rule" style="left:14px;top:27px;width:22px;height:1.5px"></div>
  <div class="abs" style="left:20px;top:45px;width:155px;height:100px;border:.6px solid var(--line)"></div>
  <div class="photo cool" role="img" aria-label="Portrait of the founding dermatologist" style="left:29px;top:54px;width:121px;height:82px"></div>
  <div class="abs" style="left:158px;top:49px;font-family:'Playfair Display',serif;font-weight:700;font-size:5.4px;color:var(--brown)">ABOUT DR. MARLOW MD, FAAD</div>
  <div class="abs" style="left:158px;top:57px;font-size:3.4px;color:var(--brown-dark)">A Doctor with a Love for Science</div>
  <div class="text" style="left:158px;top:63px;width:128px">Dr. Elena Marlow, MD, is an award-winning board-certified dermatologist, speaker and researcher. After years of study and clinical training, she built a deep passion for research, mapping skin genes in a leading laboratory and bringing that expertise to patient care and product development.<br><br>She later founded her own dermatology practice, which has been named among the best in its region. Most recently, her work has been featured in several notable beauty and health magazines, among others.</div>
  <div class="page">06</div>
</section>

<!-- 07 Market -->
<section class="slide col1 row3">
  <div class="brand">Pelarix<span class="brand-by">by dr. elena marlow</span></div>
  <div class="title" style="left:16px;top:16px;font-size:12px;line-height:1.2">Market<br>Opportunities.</div>
  <div class="abs fill-dark" style="left:16px;top:56px;width:99px;height:91px"></div>
  <div class="text" style="left:20px;top:62px;width:92px;color:#fff;font-size:3.5px;line-height:1.3">Lorem ipsum dolor sit amet, consectetuer adipiscing elit, sed diam nonummy nibh euismod tincidunt ut laoreet dolore magna aliquam erat volutpat. Ut wisi enim ad minim veniam, quis nostrud exerci tation ullamcorper suscipit lobortis nisl ut aliquip ex ea commodo consequat. Duis autem vel eum iriure dolor in hendrerit i<br><br>Lorem ipsum dolor sit amet, consectetuer adipiscing elit, sed diam nonummy nibh .</div>
  <svg class="overlay" viewBox="0 0 318 179" font-family="Poppins, sans-serif">
    <text x="208" y="36" font-size="4.8" fill="#9b5b27" text-anchor="middle" font-weight="500">Volume</text>
    <g font-size="4" fill="#333" text-anchor="end">
      <text x="137" y="47">160</text><text x="137" y="56">140</text><text x="137" y="64.5">120</text><text x="137" y="73">100</text><text x="137" y="82">80</text><text x="137" y="90.5">60</text><text x="137" y="99">40</text><text x="137" y="108">20</text><text x="137" y="116.5">0</text>
    </g>
    <g stroke="#e2e2e2" stroke-width=".4">
      <line x1="142" y1="45.5" x2="291" y2="45.5"/><line x1="142" y1="54" x2="291" y2="54"/><line x1="142" y1="63" x2="291" y2="63"/><line x1="142" y1="71.5" x2="291" y2="71.5"/><line x1="142" y1="80.5" x2="291" y2="80.5"/><line x1="142" y1="89" x2="291" y2="89"/><line x1="142" y1="98" x2="291" y2="98"/><line x1="142" y1="106.5" x2="291" y2="106.5"/>
    </g>
    <line x1="142" y1="115" x2="291" y2="115" stroke="#bbb" stroke-width=".5"/>
    <line x1="142" y1="45" x2="142" y2="115" stroke="#bbb" stroke-width=".5"/>
    <rect x="153" y="84" width="15" height="31" fill="#9b5b27"/>
    <rect x="190" y="63" width="15" height="52" fill="#6f3c17"/>
    <rect x="227" y="50" width="15" height="65" fill="#9b5b27"/>
    <rect x="264" y="56" width="15" height="59" fill="#6f3c17"/>
    <g font-size="4" fill="#333" text-anchor="middle"><text x="160" y="125">JAN</text><text x="197" y="125">FEB</text><text x="234" y="125">MAR</text><text x="271" y="125">APR</text></g>
    <circle cx="132" cy="136" r="2" fill="#9b5b27"/><text x="137" y="137.5" font-size="5" font-weight="600" fill="#6f3c17">Lorem ipsum</text>
    <circle cx="216" cy="136" r="2" fill="#9b5b27"/><text x="221" y="137.5" font-size="5" font-weight="600" fill="#6f3c17">Lorem ipsum</text>
  </svg>
  <div class="text" style="left:137px;top:140px;width:70px">Lorem ipsum dolor sit amet, consectetuer adipiscing elit, sed diam nonummy nibh euismod tincidunt ut laoreet</div>
  <div class="text" style="left:221px;top:140px;width:70px">Lorem ipsum dolor sit amet, consectetuer adipiscing elit, sed diam nonummy nibh euismod tincidunt ut laoreet</div>
  <div class="page">07</div>
</section>

<!-- 08 Section break -->
<section class="slide col2 row3 fill-dark">
  <div class="abs" style="left:0;top:59px;width:318px;text-align:center;font-family:'Playfair Display',serif;font-weight:700;font-size:13px;color:#fff">Section Break</div>
  <div class="abs" style="left:0;top:72px;width:318px;text-align:center;font-family:'Playfair Display',serif;font-weight:900;font-size:31px;letter-spacing:1px;color:#fff;line-height:1.1">SLIDE TITLE</div>
  <div class="abs" style="left:70px;top:106px;width:178px;text-align:center;font-size:4.2px;color:#f2e4d8;line-height:1.35">Lorem ipsum dolor sit amet, consectetuer adipiscing elit, sed diam nonummy nibh euismod tincid</div>
</section>

<!-- 09 Numbered list -->
<section class="slide col3 row3">
  <div class="brand">Pelarix<span class="brand-by">by dr. elena marlow</span></div>
  <div class="title" style="left:27px;top:17px;font-size:11px">Text Added Here</div>
  <div class="rule" style="left:47px;top:35px;width:54px;height:2.5px"></div>
  <div class="photo pale" role="img" aria-label="Smiling woman in a bathrobe holding a cotton pad" style="left:24px;top:37px;width:100px;height:118px"></div>
  <div class="num-dot" style="left:136px;top:49px">1</div>
  <div class="num-dot" style="left:136px;top:86px">2</div>
  <div class="num-dot" style="left:136px;top:123px">3</div>
  <div class="text" style="left:158px;top:50px;width:147px;text-align:justify">Lorem ipsum dolor sit amet, consectetuer adipiscing elit, sed diam nonummy nibh euismod tincidunt ut laoreet dolore magna aliquam erat volutpat. Ut wisi enim ad minim veniam, quis nostrud exerci tation</div>
  <div class="text" style="left:158px;top:84px;width:147px">ullamcorper suscipit lobortis nisl ut aliquip ex ea commodo consequat. Duis autem vel eum iriure dolor in hendrerit in vulputate velit esse<br><br>molestie consequat, vel illum dolore eu feugiat nulla facilisis at vero eros</div>
  <div class="text" style="left:158px;top:125px;width:147px;text-align:justify">Lorem ipsum dolor sit amet, consectetuer adipiscing elit, sed diam nonummy nibh euismod tincidunt ut laoreet dolore magna aliquam erat volutpat. Ut wisi enim ad minim veniam, quis nostrud exerci tation</div>
  <div class="page">09</div>
</section>

<!-- 10 Product story -->
<section class="slide col1 row4">
  <div class="abs fill-dark" style="left:0;top:0;width:82px;height:20px"></div>
  <div class="abs fill-dark" style="left:0;top:0;width:20px;height:95px"></div>
  <div class="brand">Pelarix<span class="brand-by">by dr. elena marlow</span></div>
  <div class="photo warm" role="img" aria-label="Dropper above a white serum bottle" style="left:28px;top:26px;width:85px;height:128px"></div>
  <div class="title" style="left:125px;top:37px;width:161px;text-align:center;font-size:11px">Text Added Here</div>
  <div class="text" style="left:128px;top:58px;width:155px;text-align:center">Lorem ipsum dolor sit amet, consectetuer adipiscing elit, sed diam nonummy nibh euismod tincidunt erat volutpat. Ut wisi enim ad minim veniam, quis nostrud exerci tation ullamcorper suscipit<br><br>lobortis nisl ut aliquip ex ea commodo consequat. Ut wisi enim ad minim veniam, quis nostrud exerci tation ullamcorper suscipit do consequat.Ut wisi enim ad minim</div>
  <div class="photo pale" role="img" aria-label="Facial mask being brushed onto a client" style="left:125px;top:92px;width:161px;height:62px"></div>
  <div class="page">10</div>
</section>

<!-- 11 Two columns -->
<section class="slide col2 row4">
  <div class="brand">Pelarix<span class="brand-by">by dr. elena marlow</span></div>
  <div class="title" style="left:9px;top:11px;font-size:11px">Text Added Here</div>
  <div class="rule" style="left:9px;top:27px;width:22px;height:1.5px"></div>
  <div class="abs" style="left:28px;top:39px;font-size:6px;color:var(--brown)">1. Text Added Here</div>
  <div class="abs" style="left:170px;top:39px;font-size:6px;color:var(--brown)">2. Text Added Here</div>
  <div class="text" style="left:28px;top:47px;width:130px;text-align:justify;line-height:1.25">Lorem ipsum dolor sit amet, cons ectetuer adipiscing elit, sed diam nonummy nibh euismod tincidunt ut laoreet dolore magna aliquam erat volutpat. Ut wisi enim ad minim veniam, quis nostrud exerci tation ullamcorper suscipit lobortis nisl ut aliquip ex ea commodo consequat.<br><br>Lorem ipsum dolor sit amet, cons ectetuer adipiscing elit, sed diam nonummy nibh euismod tincidunt ut laoreet dolore magna aliquam erat volutpat. Ut wisi enim ad minim veniam, quis nostrud exerci tation ullamcorper suscipit lobortis nisl ut aliquip ex ea commodo consequat.</div>
  <div class="text" style="left:170px;top:47px;width:130px;text-align:justify;line-height:1.25">Lorem ipsum dolor sit amet, cons ectetuer adipiscing elit, sed diam nonummy nibh euismod tincidunt ut laoreet dolore magna aliquam erat volutpat. Ut wisi enim ad minim veniam, quis nostrud exerci tation ullamcorper suscipit lobortis nisl ut aliquip ex ea commodo consequat.<br><br>Lorem ipsum dolor sit amet, cons ectetuer adipiscing elit, sed diam nonummy nibh euismod tincidunt ut laoreet dolore magna aliquam erat volutpat. Ut wisi enim ad minim veniam, quis nostrud exerci tation ullamcorper suscipit lobortis nisl ut aliquip ex ea commodo consequat.</div>
  <div class="num-box" style="left:35px;top:112px">1.</div>
  <div class="num-box" style="left:35px;top:140px">2.</div>
  <div class="num-box" style="left:177px;top:112px">1.</div>
  <div class="num-box" style="left:177px;top:140px">2.</div>
  <div class="abs" style="left:51px;top:111px;width:85px"><div style="font-size:5.4px;font-weight:500;color:var(--brown-dark)">Lorem ipsum</div><div class="text" style="position:static">Lorem ipsum dolor sit amet, consectetuer adipiscing elit, sed diam nonummy nibh</div></div>
  <div class="abs" style="left:51px;top:139px;width:85px"><div style="font-size:5.4px;font-weight:500;color:var(--brown-dark)">Lorem ipsum</div><div class="text" style="position:static">Lorem ipsum dolor sit amet, consectetuer adipiscing elit, sed diam nonummy nibh</div></div>
  <div class="abs" style="left:193px;top:111px;width:85px"><div style="font-size:5.4px;font-weight:500;color:var(--brown-dark)">Lorem ipsum</div><div class="text" style="position:static">Lorem ipsum dolor sit amet, consectetuer adipiscing elit, sed diam nonummy nibh</div></div>
  <div class="abs" style="left:193px;top:139px;width:85px"><div style="font-size:5.4px;font-weight:500;color:var(--brown-dark)">Lorem ipsum</div><div class="text" style="position:static">Lorem ipsum dolor sit amet, consectetuer adipiscing elit, sed diam nonummy nibh</div></div>
  <div class="page">11</div>
</section>

<!-- 12 Feature -->
<section class="slide col3 row4">
  <div class="brand">Pelarix<span class="brand-by">by dr. elena marlow</span></div>
  <div class="abs fill-dark" style="left:0;top:35px;width:110px;height:51px"></div>
  <div class="title" style="left:20px;top:38px;font-size:12px;line-height:1.25;color:#fff">Lorem Ipsum<br>Dolor Sit<br>Ametkeeper.</div>
  <div class="rule" style="left:36px;top:94px;width:30px"></div>
  <div class="text" style="left:20px;top:110px;width:95px">Lorem ipsum dolor sit amet, consectetuer adipiscing elit, sed diam nonummy nibh euismod tincidunt erat volutpat.<br><br>Ut wisi enim ad minim veniam, quis nostrud exerci tation ullamcorper suscipit lobortis nisl ut aliquip ex ea commodo consequat.</div>
  <div class="photo teal" role="img" aria-label="Woman looking into a round mirror" style="left:130px;top:35px;width:188px;height:79px"></div>
  <div class="text" style="left:130px;top:117px;width:178px">Lorem ipsum dolor sit amet, consectetuer adipiscing elit, sed diam nonummy nibh euismod tincidunt erat volutpat.<br><br>Ut wisi enim ad minim veniam, quis nostrud exerci tation ullamcorper suscipit lobortis nisl ut aliquip ex ea commodo consequat. Ut wisi enim ad minim veniam, quis nostrud exerci tation ullamcorper suscipit lobortis nisl ut aliquip ex ea commodo consequat.</div>
  <div class="page">12</div>
</section>

<!-- 13 Timeline -->
<section class="slide col1 row5">
  <div class="brand">Pelarix<span class="brand-by">by dr. elena marlow</span></div>
  <div class="title" style="left:9px;top:11px;font-size:11px">Text Added Here</div>
  <div class="rule" style="left:9px;top:27px;width:22px;height:1.5px"></div>
  <svg class="overlay" viewBox="0 0 318 179" font-family="Poppins, sans-serif">
    <line x1="37" y1="88" x2="281" y2="88" stroke="#9a9a9a" stroke-width=".6"/>
    <g fill="none" stroke="#9b5b27" stroke-width="1.6">
      <path d="M47 88V68a6 6 0 0 1 6-6h34a6 6 0 0 1 6 6v20"/>
      <path d="M93 88v20a6 6 0 0 0 6 6h29a6 6 0 0 0 6-6V88"/>
      <path d="M136 88V68a6 6 0 0 1 6-6h34a6 6 0 0 1 6 6v20"/>
      <path d="M182 88v20a6 6 0 0 0 6 6h29a6 6 0 0 0 6-6V88"/>
      <path d="M225 88V68a6 6 0 0 1 6-6h34a6 6 0 0 1 6 6v20"/>
    </g>
    <g fill="#9b5b27" stroke="#fff" stroke-width="1.5">
      <circle cx="70" cy="62" r="6"/><circle cx="114" cy="114" r="6"/><circle cx="159" cy="62" r="6"/><circle cx="203" cy="114" r="6"/><circle cx="248" cy="62" r="6"/>
    </g>
    <g font-size="10" fill="#6f3c17" text-anchor="middle" font-weight="500">
      <text x="70" y="84">2018</text><text x="114" y="104">2019</text><text x="159" y="84">2020</text><text x="203" y="104">2021</text><text x="248" y="84">2022</text>
    </g>
    <g fill="#9b5b27">
      <rect x="108" y="44" width="2" height="4"/><rect x="111" y="42" width="2" height="6"/><rect x="114" y="40" width="2" height="8"/>
      <path d="M198 42l8-6-3 8z"/>
      <circle cx="114" cy="130" r="2.4"/><path d="M109 137c0-3 2-4 5-4s5 1 5 4z"/>
      <circle cx="159" cy="128" r="2.6"/><rect x="157.5" y="131" width="3" height="2"/>
      <text x="248" y="133" font-size="6" text-anchor="middle">$</text><path d="M242 136h6l3 1h-9z"/>
    </g>
    <g font-size="3.6" fill="#9b5b27" text-anchor="middle" font-weight="600">
      <text x="114" y="53">LOREM IPSUM</text><text x="203" y="53">LOREM IPSUM</text>
      <text x="70" y="129">LOREM IPSUM</text><text x="159" y="143">LOREM IPSUM</text><text x="248" y="143">LOREM IPSUM</text>
    </g>
  </svg>
  <div class="abs" style="left:56px;top:128px;width:28px;height:4px"></div>
  <div class="text" style="left:98px;top:55px;width:32px;text-align:center;line-height:1.25">Lorem ipsum dolor sit amet, consectetuer adipiscing elit. Duis elit sapien, convallis</div>
  <div class="text" style="left:187px;top:55px;width:32px;text-align:center;line-height:1.25">Lorem ipsum dolor sit amet, consectetuer adipiscing elit. Duis elit sapien, convallis vel</div>
  <div class="text" style="left:54px;top:131px;width:32px;text-align:center;line-height:1.25">Lorem ipsum dolor sit amet, consectetuer adipiscing elit. Duis elit sapien</div>
  <div class="text" style="left:143px;top:145px;width:32px;text-align:center;line-height:1.25">Lorem ipsum dolor sit amet, consectetuer adipiscing elit. convallis vel enim sit amet</div>
  <div class="text" style="left:230px;top:145px;width:36px;text-align:center;line-height:1.25">Duis elit sapien, convallis vel enim sit amet, egestas commodo arcu.</div>
  <div class="page">13</div>
</section>

<!-- 14 Treatment steps -->
<section class="slide col2 row5">
  <div class="brand">Pelarix<span class="brand-by">by dr. elena marlow</span></div>
  <div class="abs fill-dark" style="left:19px;top:30px;width:273px;height:16px;color:#fff;text-align:center;font-family:'Playfair Display',serif;font-weight:700;font-size:7.4px;line-height:16px">Lorem ipsum dolor sit amet, consectetuer adipiscing elit</div>
  <div class="photo pale" role="img" aria-label="Hands giving a facial massage" style="left:19px;top:46px;width:273px;height:82px"></div>
  <div class="num-box" style="left:30px;top:123px;width:18px;height:18px;font-size:7px;line-height:18px">01</div>
  <div class="num-box" style="left:118px;top:123px;width:18px;height:18px;font-size:7px;line-height:18px">02</div>
  <div class="num-box" style="left:206px;top:123px;width:18px;height:18px;font-size:7px;line-height:18px">03</div>
  <div class="text" style="left:52px;top:131px;width:60px;line-height:1.2">Lorem ipsum Dolor sit amet Consectetur adipiscing<br><br>sed do eiusmod Tempor incididunt ut labore et dolore</div>
  <div class="text" style="left:140px;top:131px;width:60px;line-height:1.2">Lorem ipsum Dolor sit amet Consectetur adipiscing<br><br>sed do eiusmod Tempor incididunt ut labore et dolore</div>
  <div class="text" style="left:228px;top:131px;width:60px;line-height:1.2">Lorem ipsum Dolor sit amet Consectetur adipiscing<br><br>sed do eiusmod Tempor incididunt ut labore et dolore</div>
  <div class="page">14</div>
</section>

<!-- 15 Process -->
<section class="slide col3 row5">
  <div class="brand">Pelarix<span class="brand-by">by dr. elena marlow</span></div>
  <div class="title" style="left:11px;top:8px;font-size:11px">Text Added Here</div>
  <div class="rule" style="left:11px;top:25px;width:22px;height:1.5px"></div>
  <svg class="overlay" viewBox="0 0 318 179" font-family="Poppins, sans-serif">
    <g fill="none" stroke-width="4">
      <path d="M63 86a19 19 0 1 1 36 0" stroke="#6f3c17"/>
      <path d="M119 86a19 19 0 1 1 36 0" stroke="#9b5b27"/>
      <path d="M175 86a19 19 0 1 1 36 0" stroke="#6f3c17"/>
      <path d="M231 86a19 19 0 1 1 36 0" stroke="#9b5b27"/>
    </g>
    <path d="M24 84H292v-3l7 5-7 5v-3H24z" fill="#9b5b27"/>
    <g fill="#fff" stroke="#6f3c17" stroke-width=".8">
      <circle cx="81" cy="79" r="8"/><circle cx="137" cy="79" r="8"/><circle cx="193" cy="79" r="8"/><circle cx="249" cy="79" r="8"/>
    </g>
    <path d="M81 74v5l3 2" fill="none" stroke="#6f3c17" stroke-width=".8"/>
    <text x="137" y="82" font-size="7" fill="#6f3c17" text-anchor="middle">$</text>
    <g fill="none" stroke="#6f3c17" stroke-width=".7"><ellipse cx="193" cy="75" rx="4" ry="1.3"/><path d="M189 75v7c0 1 8 1 8 0v-7M189 78c0 1 8 1 8 0"/></g>
    <circle cx="250" cy="78" r="3" fill="none" stroke="#6f3c17" stroke-width=".8"/><path d="M248 80l-3 3" stroke="#6f3c17" stroke-width=".8"/>
    <g font-size="3.6" fill="#fff" text-anchor="middle" font-weight="600"><text x="81" y="87.3">Step 01</text><text x="137" y="87.3">Step 02</text><text x="193" y="87.3">Step 03</text><text x="266" y="87.3">Step 04</text></g>
    <g stroke="#9a9a9a" stroke-width=".5"><line x1="77" y1="95" x2="77" y2="103"/><line x1="133" y1="95" x2="133" y2="103"/><line x1="189" y1="95" x2="189" y2="103"/><line x1="245" y1="95" x2="245" y2="103"/></g>
  </svg>
  <div class="abs" style="left:57px;top:106px;width:40px;text-align:center"><div style="font-size:5px;font-weight:600;color:var(--brown-dark)">Lorem Ipsum</div><div class="text" style="position:static;line-height:1.2">Lorem ipsum dolor sit amet, consectetuer adipiscing elit, sed diam nonummy nibh euismod tincidunt ut laoreet dolore magna aliquam erat volutpat. Ut wisi</div></div>
  <div class="abs" style="left:113px;top:106px;width:40px;text-align:center"><div style="font-size:5px;font-weight:600;color:var(--brown-dark)">Lorem Ipsum</div><div class="text" style="position:static;line-height:1.2">Lorem ipsum dolor sit amet, consectetuer adipiscing elit, sed diam nonummy nibh euismod tincidunt ut laoreet dolore magna aliquam erat volutpat. Ut wisi</div></div>
  <div class="abs" style="left:169px;top:106px;width:40px;text-align:center"><div style="font-size:5px;font-weight:600;color:var(--brown-dark)">Lorem Ipsum</div><div class="text" style="position:static;line-height:1.2">Lorem ipsum dolor sit amet, consectetuer adipiscing elit, sed diam nonummy nibh euismod tincidunt ut laoreet dolore magna aliquam erat volutpat. Ut wisi</div></div>
  <div class="abs" style="left:225px;top:106px;width:40px;text-align:center"><div style="font-size:5px;font-weight:600;color:var(--brown-dark)">Lorem Ipsum</div><div class="text" style="position:static;line-height:1.2">Lorem ipsum dolor sit amet, consectetuer adipiscing elit, sed diam nonummy nibh euismod tincidunt ut laoreet dolore magna aliquam erat volutpat. Ut wisi</div></div>
  <div class="page">15</div>
</section>

<!-- 16 Mobile screens -->
<section class="slide col1 row6">
  <div class="brand">Pelarix<span class="brand-by">by dr. elena marlow</span></div>
  <div class="title" style="left:15px;top:12px;font-size:11px">Text Added Here</div>
  <div class="rule" style="left:15px;top:28px;width:22px;height:1.5px"></div>
  <div class="text" style="left:15px;top:36px;width:95px">Lorem ipsum dolor sit amet, consectetuer adipiscing elit, sed diam nonummy nibh euismod tincidunt ut laoreet dolore magna aliquam erat volutpat. Ut wisi enim ad minim veniam,<br><br>quis nostrud exerci tation ullamcorper suscipit lobortis nisl ut aliquip quat. Duis autem vel eum</div>
  <div class="abs fill-dark" style="left:0;top:95px;width:110px;height:67px"></div>
  <div class="num-box" style="left:17px;top:100px;width:9px;height:9px;line-height:9px;background:#fff;color:var(--brown-dark)">1.</div>
  <div class="num-box" style="left:17px;top:121px;width:9px;height:9px;line-height:9px;background:#fff;color:var(--brown-dark)">2.</div>
  <div class="num-box" style="left:17px;top:142px;width:9px;height:9px;line-height:9px;background:#fff;color:var(--brown-dark)">3.</div>
  <div class="abs" style="left:30px;top:100px;width:75px;color:#fff"><div style="font-family:'Playfair Display',serif;font-size:3.8px;font-weight:700">Lorem ipsum</div><div style="font-size:2.7px;line-height:1.3">Lorem ipsum dolor sit amet, consectetuer adipiscing elit, sed diam nonummy nibh euismod tincid</div></div>
  <div class="abs" style="left:30px;top:121px;width:75px;color:#fff"><div style="font-family:'Playfair Display',serif;font-size:3.8px;font-weight:700">Lorem ipsum</div><div style="font-size:2.7px;line-height:1.3">Lorem ipsum dolor sit amet, consectetuer adipiscing elit, sed diam nonummy nibh euismod tincid</div></div>
  <div class="abs" style="left:30px;top:142px;width:75px;color:#fff"><div style="font-family:'Playfair Display',serif;font-size:3.8px;font-weight:700">Lorem ipsum</div><div style="font-size:2.7px;line-height:1.3">Lorem ipsum dolor sit amet, consectetuer adipiscing elit, sed diam nonummy nibh euismod tincid</div></div>
  <div class="photo" role="img" aria-label="Faint world map behind the screens" style="left:150px;top:45px;width:150px;height:90px;background:radial-gradient(ellipse at center,#eeeeee 0%,#f6f6f6 55%,#ffffff 80%)"></div>
  <div class="abs" style="left:138px;top:22px;width:38px;height:86px;border:1.4px solid #2a2a2a;border-radius:4px;background:#fff;padding:6px 4px">
    <div style="font-family:'Playfair Display',serif;font-weight:700;font-size:4px;color:var(--brown);line-height:1.1">Lorem<br>ipsum dolor</div>
    <div style="margin:8px auto 4px;width:6px;height:5px;border:.5px solid var(--muted)"></div>
    <div style="font-size:2px;line-height:1.3;color:var(--muted)">To introduce the students to the changing landscape of marketing and equip them with knowledge and tools to navigate the digital world.</div>
  </div>
  <div class="abs" style="left:188px;top:47px;width:38px;height:83px;border:1.4px solid #2a2a2a;border-radius:4px;background:#fff;padding:16px 4px 4px">
    <div style="font-family:'Playfair Display',serif;font-weight:700;font-size:3.8px;color:var(--brown);line-height:1.1">Dolor sit<br>amet, conse</div>
    <div style="margin:4px auto;width:6px;height:6px;border:.5px solid var(--muted);border-radius:50%"></div>
    <div style="font-size:2px;line-height:1.3;color:var(--muted)">You will learn core concepts and ideas in digital marketing as well as how to use different tools and strategies to plan your campaigns.</div>
  </div>
  <div class="abs" style="left:237px;top:75px;width:38px;height:85px;border:1.4px solid #2a2a2a;border-radius:4px;background:#fff;padding:18px 4px 4px">
    <div style="font-family:'Playfair Display',serif;font-weight:700;font-size:3.8px;color:var(--brown);line-height:1.1">Consec</div>
    <div style="margin:8px auto 4px;width:6px;height:6px;border:.5px solid var(--muted);border-radius:50%"></div>
    <div style="font-size:2px;line-height:1.3;color:var(--muted)">You are required to pass 80% of the evaluation test to obtain the certificate. The test can only be taken 3 times.</div>
  </div>
  <div class="page">15</div>
</section>

<!-- 17 Team -->
<section class="slide col2 row6">
  <div class="brand">Pelarix<span class="brand-by">by dr. elena marlow</span></div>
  <div class="title" style="left:11px;top:10px;font-size:11px">Text Added Here</div>
  <div class="rule" style="left:11px;top:26px;width:22px;height:1.5px"></div>
  <div class="text" style="left:11px;top:33px;width:296px;text-align:justify;line-height:1.3">Lorem ipsum dolor sit amet, consectetuer adipiscing elit, sed diam nonummy nibh euismod tincidunt ut laoreet dolore magna aliquam erat volutpat. Ut wisi enim ad minim veniam, quis nostrud exerci tation ullamcorper suscipit lobortis nisl ut aliquip ex ea commodo consequat. Duis autem vel eum iriure dolor in hendrerit in vulputate velit esse molestie consequat, vel illum dolore eu feugiat nulla facilisis at vero eros et accumsan et iusto odio dignissim qui blandit praesent luptatum zzril delenit augue duis dolore te feugait nulla facilisi.<br><br>Lorem ipsum dolor sit amet, cons ectetuer adipiscing elit, sed diam nonummy nibh euismod tincidunt ut laoreet dolore magna aliquam erat volutpat. Ut wisi enim ad minim veniam, quis nostrud exerci tation ullamcorper suscipit lobortis nisl ut aliquip ex ea commodo.</div>
  <div class="abs fill-dark" style="left:0;top:95px;width:318px;height:58px"></div>
  <div class="photo pale" role="img" aria-label="Team member portrait" style="left:30px;top:79px;width:26px;height:26px;border-radius:50%;border:1.5px solid #fff"></div>
  <div class="photo warm" role="img" aria-label="Team member portrait" style="left:107px;top:79px;width:26px;height:26px;border-radius:50%;border:1.5px solid #fff"></div>
  <div class="photo pale" role="img" aria-label="Team member portrait" style="left:182px;top:79px;width:26px;height:26px;border-radius:50%;border:1.5px solid #fff"></div>
  <div class="photo warm" role="img" aria-label="Team member portrait" style="left:259px;top:79px;width:26px;height:26px;border-radius:50%;border:1.5px solid #fff"></div>
  <div class="abs" style="left:13px;top:108px;width:60px;text-align:center;color:#fff"><div style="font-family:'Playfair Display',serif;font-weight:700;font-size:6px">John Smith</div><div style="font-size:2.6px;line-height:1.3;margin-top:2px">ipsum dolor sit amet, cons ectetuer adipiscing elit, sed diam nonummy nibh euismod tincidunt ut laoreet dolore magna aliquam erat volutpat. Ut wisi enim ad minim veniam, quis nostrud</div></div>
  <div class="abs" style="left:90px;top:108px;width:60px;text-align:center;color:#fff"><div style="font-family:'Playfair Display',serif;font-weight:700;font-size:6px">Millie Smith</div><div style="font-size:2.6px;line-height:1.3;margin-top:2px">ipsum dolor sit amet, cons ectetuer adipiscing elit, sed diam nonummy nibh euismod tincidunt ut laoreet dolore magna aliquam erat volutpat. Ut wisi enim ad minim veniam, quis nostrud</div></div>
  <div class="abs" style="left:165px;top:108px;width:60px;text-align:center;color:#fff"><div style="font-family:'Playfair Display',serif;font-weight:700;font-size:6px">John Smith</div><div style="font-size:2.6px;line-height:1.3;margin-top:2px">ipsum dolor sit amet, cons ectetuer adipiscing elit, sed diam nonummy nibh euismod tincidunt ut laoreet dolore magna aliquam erat volutpat. Ut wisi enim ad minim veniam, quis nostrud</div></div>
  <div class="abs" style="left:242px;top:108px;width:60px;text-align:center;color:#fff"><div style="font-family:'Playfair Display',serif;font-weight:700;font-size:6px">Millie Smith</div><div style="font-size:2.6px;line-height:1.3;margin-top:2px">ipsum dolor sit amet, cons ectetuer adipiscing elit, sed diam nonummy nibh euismod tincidunt ut laoreet dolore magna aliquam erat volutpat. Ut wisi enim ad minim veniam, quis nostrud</div></div>
</section>

<!-- 18 Thank you -->
<section class="slide col3 row6">
  <div class="abs" style="left:0;top:15px;width:318px;text-align:center;font-family:'Playfair Display',serif;font-weight:900;font-size:23px;color:var(--brown);line-height:1">Pelarix</div>
  <div class="abs" style="left:0;top:42px;width:318px;text-align:center;font-size:6.4px;color:var(--brown)">by dr. elena marlow</div>
  <div class="abs" style="left:40px;top:82px;width:90px;text-align:right;font-family:'Playfair Display',serif;font-weight:900;font-size:21px;color:var(--brown);line-height:1.3">Thank<br>You</div>
  <div class="photo warm" role="img" aria-label="Woman relaxing at a spa beside candles" style="left:137px;top:65px;width:113px;height:87px"></div>
  <div class="abs fill-dark" style="left:254px;top:65px;width:14px;height:87px"></div>
  <div class="abs" style="left:261px;top:108px;transform:translate(-50%,-50%) rotate(-90deg);font-size:6px;letter-spacing:2.2px;color:#fff;white-space:nowrap">pelarix.com</div>
</section>

</div>
</body>
</html>
```